New homepage concept needed for online reading programs website

About the Academy of Literacy Growth:
The Institute teaches online summer Brightpage Readers programs for entering fourth graders, offered through partnerships with universities, colleges, and municipalities nationwide. The goal of the program is to build Brightpage Readers (long-word decoding, fluency and comprehension), and foster a lifelong love of books and reading.

Aims & Target Market:
The Institute has developed a new format of its online reading program for fourth graders, which includes live small-group video classes taught by a professional reading teacher. The Institute seeks a mock-up of a homepage of the website used to market this new program. The primary audience for this website is the parents of these 4th graders. Traffic to this website is driven by direct-marketing campaigns directed at parents and students.

Live classes for children are completely new in online education, unlike anything else in the marketplace, and parents therefor have no experience with them. The successful homepage mock-up will include illustrations or photographs that allow visitors to immediately grasp/understand the new format, without relying on a written description. Additionally, the successful homepage concept will make the program, and the video classes in particular, feel fun and appealing to kids and parents alike.

There are three main elements to the program, and each needs to be represented graphically on the homepage, with particular emphasis on the small-group video classes:
1. Live small-group video classes (weekly for six weeks):
a. During video class discussions, the student’s computer (or tablet) screen is filled with live video frames of the teacher and the other students. The video frame for the teacher is larger, and the other students appear in smaller frames.
b. During other video class instruction, the teacher uses a presentation screen to display pages of a book or a “whiteboard” used for instructional activities.
c. The homepage mock-up could include a screenshot of the video classes themselves, with children looking engaged and a teacher leading them in discussion. We have included a screen shot of one of these classes for reference, but do not feel constrained to represent this screen realistically (as shown here). It can be changed around – teacher in the center, etc.). Alternately, if there is a graphic other than a screen shot that you feel could be used to bring across the concept of the video classes, feel free.
2. Individualized online instruction
a. Graphics could include screenshots of the video lessons students complete in between these weekly classes and/or images of a child or children at computer(s).
3. Independent reading in great books
a. Graphics could include some or all of the program books, which can be pulled from our current website (link below), and/or images of a child or children reading.

An example of our current online program website can be seen at http://fenwick.webliteracystudio.example/4/Home. Please reference this site for information on program goals, books/materials, and site navigation.
The successful design will be welcoming and inviting, and allow parents and students to immediately grasp what the programs are, with particular emphasis on the live small-group video classes.

Copy and Specifications:
Sample copy has been provided for reference, as well as a screen shot of our sample classes to show what students will see on screen. Also included are stills of our online video lessons to illustrate the online instruction aspect.

```html
<!DOCTYPE html>
<html lang="en">
<head>
<meta charset="utf-8">
<title>Brightpage Readers – Online Program for 4th and 5th Graders</title>
<link href="https://fonts.googleapis.com/css2?family=Open+Sans:wght@400;600;700&family=Oswald:wght@400;500;700&display=swap" rel="stylesheet">
<style>
:root{
  --green:#4a9a12;
  --green-dark:#3a7d0c;
  --lime:#7cbd1e;
  --orange:#f7941d;
  --orange-dark:#e27a0b;
  --blue:#2f63b4;
  --blue-dark:#234f96;
  --gold:#e4b433;
  --ink:#333;
  --muted:#777;
  --light:#f1f1f1;
  --footer:#2b2b2b;
  --footer-bottom:#1f1f1f;
  --white:#fff;
}
*{margin:0;padding:0;box-sizing:border-box}
html,body{width:849px;height:1200px;overflow:hidden;background:var(--white);font-family:'Open Sans',sans-serif;color:var(--ink)}
.page{position:relative;width:849px;height:1200px}

/* header */
.site-header{position:absolute;top:0;left:0;width:849px;height:108px}
.brand{position:absolute;left:93px;top:26px}
.brand-name{font-family:'Open Sans',sans-serif;font-weight:600;font-size:26px;color:var(--green-dark);line-height:1}
.brand-tag{font-size:11px;color:var(--muted);font-weight:600;margin-top:6px}
.group-select{position:absolute;right:82px;top:38px;display:flex;align-items:center;gap:10px;font-size:8px;color:var(--muted);font-weight:600}
.group-select .box{width:110px;height:20px;border:1px solid #ccc;border-radius:2px;font-size:8px;padding:4px 6px;color:#999;position:relative}
.group-select .box::after{content:"";position:absolute;right:6px;top:8px;border:4px solid transparent;border-top-color:#999}

.main-nav{position:absolute;top:108px;left:0;width:849px;height:19px;background:linear-gradient(var(--lime),var(--green-dark))}
.main-nav ul{list-style:none;display:flex;justify-content:center;height:100%}
.main-nav li{color:var(--white);font-size:8px;font-weight:700;padding:0 18px;line-height:19px;border-right:1px solid rgba(255,255,255,.25)}
.main-nav li:last-child{border-right:0}

/* hero */
.hero{position:absolute;top:127px;left:0;width:849px;height:298px}
.hero-photo{position:absolute;inset:0;background:linear-gradient(100deg,#c9b49a 0%,#e8d9c4 30%,#f3ece2 55%,#cfd7de 100%)}
.hero-panel{position:absolute;left:524px;top:54px;width:302px;height:215px;background:rgba(40,40,40,.72);padding:16px 16px;color:var(--white)}
.hero-panel h2{font-family:'Oswald',sans-serif;font-weight:500;color:var(--gold);font-size:24px;letter-spacing:2px;margin-bottom:6px}
.hero-panel p{font-size:7.5px;line-height:1.5;margin-bottom:8px}
.hero-panel ul{list-style:none}
.hero-panel li{font-size:7.5px;line-height:2;display:flex;align-items:center;gap:6px}
.hero-panel li::before{content:"";width:7px;height:7px;border-radius:50%;background:var(--lime);flex:none}
.hero-dots{position:absolute;right:30px;bottom:12px;display:flex;gap:5px}
.hero-dots span{width:7px;height:7px;border-radius:50%;background:#999}
.hero-dots span.on{background:var(--orange)}

/* program */
.program{position:absolute;top:528px;left:0;width:849px;text-align:center}
.program h1{font-family:'Oswald',sans-serif;font-weight:400;font-size:18px;color:#555;letter-spacing:.5px}
.program h1 strong{color:var(--green);font-weight:700}
.program .rule{width:220px;height:1px;background:#ddd;margin:6px auto 10px}
.program p{font-size:8px;color:var(--muted);width:400px;margin:0 auto;line-height:1.6}

.cards{position:absolute;top:628px;left:93px;display:flex;gap:27px}
.card{width:200px;height:221px;padding:12px 13px;color:var(--white);position:relative}
.card.live{background:linear-gradient(var(--lime),var(--green))}
.card.individual{background:linear-gradient(#fbab3c,var(--orange-dark))}
.card.independent{background:linear-gradient(#3d76c8,var(--blue-dark))}
.card h3{font-family:'Oswald',sans-serif;font-weight:700;font-size:23px;line-height:1}
.card .sub{font-family:'Oswald',sans-serif;font-size:10px;letter-spacing:.5px;margin-bottom:7px}
.card .media{height:80px;border:3px solid var(--white)}
.card p{font-size:7.5px;line-height:1.55;margin-top:8px}
.card .more{position:absolute;left:13px;bottom:12px;font-size:8px;font-weight:700;padding:5px 11px;border-radius:2px}
.live .more{background:var(--green-dark)}
.individual .more{background:#c96a08}
.independent .more{background:#1c3f7a}

/* info strip */
.info-strip{position:absolute;top:948px;left:71px;width:693px;height:65px;background:var(--light);display:flex;align-items:center;justify-content:space-between;padding:0 26px}
.info-item{display:flex;align-items:center;gap:10px}
.info-item .label{font-size:8px;color:var(--muted);font-weight:600}
.info-item .value{font-family:'Oswald',sans-serif;font-size:16px;color:var(--orange);line-height:1.1}
.info-item.center{text-align:center;display:block}
.info-item.center .value{color:var(--green);font-size:19px}
.icon-circle{width:30px;height:30px;border-radius:50%;background:#8a8a8a;display:flex;align-items:center;justify-content:center}

/* footer */
.site-footer{position:absolute;top:1039px;left:0;width:849px;height:121px;background:var(--footer);color:#bbb}
.footer-brand{position:absolute;left:93px;top:32px;display:flex;align-items:center;gap:8px}
.footer-brand .mark{width:14px;height:14px;background:var(--gold)}
.footer-brand .name{font-family:'Oswald',sans-serif;font-weight:400;font-size:24px;color:var(--white);line-height:1;letter-spacing:1px}
.footer-brand .tag{font-size:8px;color:var(--gold);margin-top:3px}
.footer-address{position:absolute;left:317px;top:36px;font-size:8px;line-height:1.6}
.footer-contact{position:absolute;left:467px;top:36px;font-size:8px;line-height:1.6;color:var(--lime)}
.reg-button{position:absolute;left:628px;top:36px;width:130px;text-align:center;background:var(--green);color:var(--white);font-size:9px;font-weight:700;padding:10px 0}
.footer-bottom{position:absolute;top:1160px;left:0;width:849px;height:40px;background:var(--footer-bottom);display:flex;align-items:center;justify-content:space-between;padding:0 40px 0 93px}
.footer-bottom small{font-size:7.5px;color:#888}
.social{display:flex;gap:6px}
.social span{width:16px;height:16px;border-radius:50%;border:1px solid #777}
</style>
</head>
<body>
<div class="page">

  <header class="site-header">
    <div class="brand">
      <div class="brand-name">Brightpage Readers</div>
      <div class="brand-tag">Online Program for 4th and 5th Graders</div>
    </div>
    <div class="group-select">
      <span>SELECT A UNIVERSITY/ORG GROUP</span>
      <div class="box">Choose Your Group</div>
    </div>
  </header>

  <nav class="main-nav">
    <ul>
      <li>HOME</li><li>LIVE CLASSES</li><li>DECODING SKILLS</li><li>FLUENCY</li><li>COMPREHENSION</li><li>FAQ</li><li>ENROLL</li>
    </ul>
  </nav>

  <section class="hero">
    <div class="hero-photo" role="img" aria-label="Photo of two children smiling and working together at a laptop"></div>
    <div class="hero-panel">
      <h2>FENWICK</h2>
      <p>This summer Fenwick University joins the Academy of Literacy Growth to offer an online reading program for students entering fourth and fifth grade, built around live classes.</p>
      <ul>
        <li>Build long-word decoding skills</li>
        <li>Read with fluency and expression</li>
        <li>Improve comprehension skills</li>
        <li>Develop a lifelong love of reading</li>
      </ul>
    </div>
    <div class="hero-dots"><span class="on"></span><span></span><span></span><span></span></div>
  </section>

  <section class="program">
    <h1>THIS FIVE WEEK <strong>PROGRAM</strong></h1>
    <div class="rule"></div>
    <p>A reading teacher from the Academy leads each small group through the lessons, with online practice between classes and great books to read at home.</p>
  </section>

  <div class="cards">
    <article class="card live">
      <h3>LIVE SMALL</h3>
      <div class="sub">GROUP VIDEO CLASSES</div>
      <div class="media" role="img" aria-label="Photo of a teacher and children in a live video class" style="background:linear-gradient(135deg,#d9c6a8,#8fb36a)"></div>
      <p>A reading teacher leads live video classes where students see and hear each other every week.</p>
      <span class="more">READ MORE</span>
    </article>
    <article class="card individual">
      <h3>INDIVIDUALIZED</h3>
      <div class="sub">ONLINE INSTRUCTION</div>
      <div class="media" role="img" aria-label="Screenshot of an online video lesson on a computer screen" style="background:linear-gradient(135deg,#f4e3c3,#c9b08a)"></div>
      <p>Short online lessons between classes let each student practice skills at their own pace.</p>
      <span class="more">READ MORE</span>
    </article>
    <article class="card independent">
      <h3>INDEPENDENT</h3>
      <div class="sub">READING IN GREAT BOOKS</div>
      <div class="media" role="img" aria-label="Covers of the program books arranged together" style="background:linear-gradient(135deg,#9fb8d8,#d8a15c)"></div>
      <p>Students read award-winning books at home and share their ideas in class discussions.</p>
      <span class="more">READ MORE</span>
    </article>
  </div>

  <section class="info-strip">
    <div class="info-item">
      <div class="icon-circle">
        <svg width="14" height="16" viewBox="0 0 14 16"><rect x="1" y="1" width="12" height="14" fill="none" stroke="#fff" stroke-width="1.5"/><path d="M4 5h6M4 8h6M4 11h4" stroke="#fff" stroke-width="1.3"/></svg>
      </div>
      <div><div class="label">REGISTRATION</div><div class="value">INFORMATION</div></div>
    </div>
    <div class="info-item center">
      <div class="label">MORE INFORMATION</div>
      <div class="value">CALL (800) 555-0142</div>
    </div>
    <div class="info-item">
      <div class="icon-circle">
        <svg width="14" height="14" viewBox="0 0 14 14"><circle cx="7" cy="4.5" r="3" fill="#fff"/><path d="M1 14c0-4 2.7-6 6-6s6 2 6 6z" fill="#fff"/></svg>
      </div>
      <div><div class="label">CLICK HERE TO</div><div class="value">ENROLL NOW</div></div>
    </div>
  </section>

  <footer class="site-footer">
    <div class="footer-brand">
      <span class="mark"></span>
      <div><div class="name">FENWICK</div><div class="tag">Summer Reading Program</div></div>
    </div>
    <div class="footer-address">48 Harbor Lane<br>Westbrook, OR 97301</div>
    <div class="footer-contact">(800) 555-0142<br>hello@brightpage.example</div>
    <div class="reg-button">REGISTRATION INFO</div>
  </footer>
  <div class="footer-bottom">
    <small>© 2013 Brightpage Readers. All Rights Reserved.</small>
    <div class="social"><span></span><span></span><span></span><span></span><span></span></div>
  </div>

</div>
</body>
</html>
```